Brightwell Giving Inc

We need a full re-design of our non-profit organization website (www.brightwellgiving.org). Ideally, we are looking to make it more attractive, user-friendly, and interactive with our business model.

Please make sure to user colors that ago with our logo.

We need a homepage done and we also need a content page done where we will use for the other pages to fill with content.

Target Market(s)

Clothes/textiles donations.

Industry/Entity Type

Charity

Number of Pages Required

2 page

Colors

Designer to choose colors to be used in the design.

Requirements
Must have
• It must match the styling of our logo and same colors as current website. (www.brightwellgiving.org)
Nice to have
• Sleek homepage that is easy to understand and get our main points across.

```html
<!DOCTYPE html>
<html lang="en">
<head>
<meta charset="utf-8">
<title>Brightwell Giving — Home</title>
<link href="https://fonts.googleapis.com/css2?family=Roboto:wght@400;500;700&family=Roboto+Condensed:wght@400;700&display=swap" rel="stylesheet">
<style>
:root{
  --green:#3e6b1f;
  --green-dark:#2f5516;
  --green-text:#4b7a26;
  --orange:#f2a51a;
  --gray-bg:#ececec;
  --ink:#222;
  --footer:#1f1f1f;
  --white:#fff;
}
*{margin:0;padding:0;box-sizing:border-box}
html,body{width:1200px;height:4196px;overflow:hidden}
body{position:relative;background:var(--white);font-family:'Roboto',Arial,sans-serif;color:var(--ink)}
.abs{position:absolute}

/* top bar */
.topbar{left:0;top:0;width:1200px;height:70px;background:var(--green)}
.contact-item{top:16px;display:flex;gap:10px;align-items:center;color:var(--white);font-size:12px;line-height:15px}
.contact-item b{font-size:14px;font-weight:700;display:block}
.icon-box{width:28px;height:24px;background:var(--ink);border-radius:3px;display:flex;align-items:center;justify-content:center}
.donate-btn{left:893px;top:22px;width:96px;height:26px;border:2px solid var(--orange);color:var(--orange);font-size:11px;display:flex;align-items:center;justify-content:center}

/* header */
.brand{left:201px;top:88px;display:flex;align-items:center;gap:10px}
.brand-mark{width:50px;height:50px;background:var(--orange)}
.brand-name{font-family:'Roboto Condensed',sans-serif;font-weight:700;font-size:27px;color:var(--green);line-height:28px}
.brand-tag{font-size:14px;color:var(--green-dark);line-height:18px}
.search{left:724px;top:99px;width:222px;height:42px;border:3px solid var(--ink);display:flex}
.search span{flex:1;font-family:'Roboto Condensed',sans-serif;font-weight:700;font-size:18px;padding:8px 10px;color:var(--ink)}
.search i{width:44px;background:var(--orange);display:flex;align-items:center;justify-content:center;border-left:3px solid var(--ink)}
.nav{left:0;top:173px;width:1200px;height:45px;border-top:2px solid var(--green);display:flex;padding-left:207px;gap:42px;align-items:center}
.nav a{font-family:'Roboto Condensed',sans-serif;font-size:15px;color:var(--green);text-decoration:none;font-weight:700;height:45px;display:flex;align-items:center}
.nav a.active{color:var(--orange);border-bottom:3px solid var(--orange)}

/* hero */
.hero{left:0;top:218px;width:1200px;height:515px;background:linear-gradient(90deg,#0c0c0c 0%,#2a2a2a 40%,#4a4a4a 60%,#3a2230 85%,#7a2f5a 100%)}
.hero-title{left:654px;top:326px;color:var(--white);font-family:'Roboto Condensed',sans-serif;font-size:40px;line-height:50px;text-shadow:0 2px 4px rgba(0,0,0,.5)}

/* welcome */
.section-title{width:1200px;left:0;text-align:center;font-family:'Roboto Condensed',sans-serif;font-weight:700}
.welcome-box{left:190px;top:805px;width:818px;min-height:276px;border:3px solid var(--green-text);padding:34px 40px 24px;text-align:center;font-size:17px;line-height:27px}
.welcome-title{left:480px;top:780px;width:240px;background:var(--white);text-align:center;font-family:'Roboto Condensed',sans-serif;font-weight:700;font-size:44px;line-height:52px}

/* about */
.about{left:0;top:1147px;width:1200px;height:601px;background:linear-gradient(135deg,#4e7a2c,#3a6220 50%,#4c7a2a)}
.about-text{left:210px;top:1290px;width:780px;text-align:center;color:var(--white);font-weight:700;font-size:18px;line-height:29px}
.about-list{left:0;top:1505px;width:1200px;text-align:center;color:var(--white);font-family:'Roboto Condensed',sans-serif;font-weight:700;font-size:19px;line-height:33px}

/* how it works */
.how{left:0;top:1748px;width:1200px;height:1441px;background:var(--gray-bg)}
.step-num{width:102px;height:102px;border:3px solid var(--green-text);border-radius:50%;display:flex;align-items:center;justify-content:center;font-size:50px;color:var(--green-text)}
.step-head{font-family:'Roboto Condensed',sans-serif;font-weight:700;font-size:19px;color:var(--green-text);text-transform:uppercase}
.step-text{font-size:17px;line-height:28px;color:var(--green-text)}
.read-more{width:128px;height:40px;background:var(--green-dark);color:var(--white);font-size:17px;display:flex;align-items:center;justify-content:center}
.photo{border-radius:2px}

/* news */
.card{width:270px;height:350px;background:var(--white);padding:14px 16px}
.card.lift{box-shadow:0 3px 12px rgba(0,0,0,.25)}
.card-meta{font-size:10px;line-height:16px;color:#777;font-weight:700}
.card-meta b{color:var(--green)}
.card-logo{margin-top:10px;height:140px;border:3px solid var(--orange);display:flex;align-items:center;justify-content:center;font-family:'Roboto Condensed',sans-serif;font-weight:700;font-size:17px;color:var(--ink)}
.card-date{margin-top:10px;display:flex;gap:6px;align-items:center;font-size:10px;font-weight:700;color:var(--green)}
.card-text{margin-top:6px;font-size:9px;line-height:12px;color:#555;text-transform:uppercase;padding-left:24px}
.card-btn{margin:14px auto 0;width:88px;height:30px;border:2px solid var(--orange);color:var(--orange);font-size:10px;display:flex;align-items:center;justify-content:center}

/* contact */
.contact{left:0;top:3742px;width:1200px;height:384px;background:var(--green)}
.office{width:260px;text-align:center;color:var(--white);font-family:'Roboto Condensed',sans-serif;font-weight:700}
.office h3{font-size:17px;margin-bottom:26px}
.office p{font-size:17px;line-height:21px}
.footer{left:0;top:4126px;width:1200px;height:70px;background:var(--footer);color:#ccc;font-family:'Roboto Condensed',sans-serif;font-weight:700;font-size:15px;display:flex;align-items:center;justify-content:center}
</style>
</head>
<body>

<!-- top bar -->
<div class="abs topbar"></div>
<div class="abs contact-item" style="left:201px">
  <div class="icon-box"><svg width="16" height="12" viewBox="0 0 16 12"><rect x="0.5" y="0.5" width="15" height="11" fill="none" stroke="#f2a51a"/><path d="M1 1l7 6 7-6" fill="none" stroke="#f2a51a"/></svg></div>
  <div><b>Email:</b>info@brightwellgiving.org</div>
</div>
<div class="abs contact-item" style="left:388px">
  <div class="icon-box"><svg width="14" height="14" viewBox="0 0 24 24"><path d="M6.6 10.8a15 15 0 006.6 6.6l2.2-2.2a1 1 0 011-.25 11.4 11.4 0 003.6.57 1 1 0 011 1V20a1 1 0 01-1 1A17 17 0 013 4a1 1 0 011-1h3.5a1 1 0 011 1c0 1.25.2 2.45.57 3.6a1 1 0 01-.25 1z" fill="#f2a51a"/></svg></div>
  <div><b>Phone:</b>Toll Free: (855)-555-0142<br>New York: 518-555-0190</div>
</div>
<div class="abs donate-btn">Donate Now</div>

<!-- header -->
<div class="abs brand">
  <div class="brand-mark"></div>
  <div>
    <div class="brand-name">BRIGHTWELL GIVING</div>
    <div class="brand-tag">Think Globally while Donating Locally</div>
  </div>
</div>
<div class="abs search">
  <span>SEARCH</span>
  <i><svg width="22" height="22" viewBox="0 0 24 24"><circle cx="10" cy="10" r="7" fill="none" stroke="#222" stroke-width="3"/><path d="M15 15l7 7" stroke="#222" stroke-width="3"/></svg></i>
</div>
<nav class="abs nav">
  <a class="active">HOME</a><a>MISSIONS</a><a>HOW IT WORKS</a><a>ABOUT US</a><a>SPONSORS</a><a>NEWS</a><a>DONATE</a><a>WALL OF NEEDS</a>
</nav>

<!-- hero -->
<div class="abs hero" role="img" aria-label="Black and white photo of a child looking out, beside many colourful raised hands"></div>
<div class="abs hero-title">THINK GLOBALLY WHILE<br>DONATING LOCALLY</div>

<!-- welcome -->
<div class="abs welcome-box">Brightwell Giving is a non-profit organization that was created for one purpose: helping the less fortunate in our country’s time of greatest need. Started in 2007, Brightwell Giving has been a dedicated member of its local communities over the past four years. The company’s clothing collection efforts have allowed it to provide some of the neediest members of the community to clothe themselves and their families. The company’s goal is to ensure that some of the most basic needs of the community’s members are met thru the philanthropic efforts of the organizations members and contributors.</div>
<div class="abs welcome-title">WELCOME</div>

<!-- about -->
<div class="abs about" role="img" aria-label="Green-tinted photo of smiling children"></div>
<div class="abs section-title" style="top:1200px;color:#fff;font-size:42px">ABOUT US</div>
<div class="abs about-text">We are a family based non-profit organization in the name of Brightwell Giving Inc . We started this foundation in effort to help the community and unite it’s effort to give back to the less fortunate by the means of donating unwanted used clothing. This is not our primary business, but we did undertsand it was our time to step in and help the communites and people in need. Since September 2011, we have personally donated over $50,000 dollars to various foundation and organization who are already helping local communities.</div>
<div class="abs about-list">WE ARE AN OPEN BOOK ORGANIZATION<br>WE ARE A TRUE 501(C)(3) NON-PROFIT ORGANIZATION<br>OUR GOAL IS TO BE WITH AND WITHIN THE COMMUNITY<br>SUPPORT ANTI-GUN VIOLENCE<br>HELP DISASTER VICTIMS OF HURRICANE IRENE<br>HELP HILLSIDE FAMILY SUPPORT SOCIETY</div>

<!-- how it works -->
<div class="abs how"></div>
<div class="abs section-title" style="top:1805px;font-size:42px">HOW IT WORKS</div>

<div class="abs step-num" style="left:193px;top:1888px">1</div>
<div class="abs step-head" style="left:193px;top:2022px">Drop off clothing at your closest donation bin.</div>
<div class="abs step-text" style="left:193px;top:2064px;width:485px">We have different collection procedures. For outdoors we can place a donation bin, a metal container about 48”L X 48”WX66”H. Inside collecting we would use a commercial laundry bin 48”LX29”WX55”H. We can also schedule pick up of donated clothing, where we would supply a plastic bag and the donated clothing would be left. Outside or in dryway for a scheduled pick up.</div>
<div class="abs photo" style="left:700px;top:1952px;width:350px;height:313px;background:linear-gradient(160deg,#e9e9e9,#c9b39a 55%,#4a6a8c)" role="img" aria-label="Photo of a man and woman holding donation boxes of clothing"></div>

<div class="abs step-num" style="left:559px;top:2294px">2</div>
<div class="abs photo" style="left:176px;top:2377px;width:336px;height:252px;background:linear-gradient(170deg,#e6e6e6,#c77aa8 35%,#c49a68 70%,#d7d7d7)" role="img" aria-label="Photo of a cardboard donation box filled with colourful clothes"></div>
<div class="abs step-head" style="left:557px;top:2422px">We pick it up and take it to our sorting facility</div>
<div class="abs step-text" style="left:557px;top:2462px;width:470px">After our drivers pick up the clothing from our designated donation locations, the items are taken to our sorting facility where they are separated into three categories. Ten percent of the clothing is designated as category A which is higher-end pieces that are like-new or only slightly used.</div>
<div class="abs read-more" style="left:557px;top:2650px">read more</div>

<div class="abs step-num" style="left:193px;top:2721px">3</div>
<div class="abs step-head" style="left:193px;top:2850px">Charities get clothing. We pay you for the clothes.</div>
<div class="abs step-text" style="left:193px;top:2890px;width:480px">Once we are done distributing our donated clothing to their appropriate channels, the proceeds from the sales are distributed in two ways. The first distribution is in the form of donations to local charities and benevolent organizations.</div>
<div class="abs read-more" style="left:193px;top:3054px">read more</div>
<div class="abs photo" style="left:694px;top:2797px;width:318px;height:243px;background:linear-gradient(150deg,#d8d2c8,#6f8fb0 45%,#c46a8a 80%)" role="img" aria-label="Photo of volunteers sorting clothes into shopping bags"></div>

<!-- news -->
<div class="abs section-title" style="top:3237px;font-size:44px;color:var(--green-text)">NEWS</div>

<div class="abs card lift" style="left:187px;top:3337px">
  <div class="card-meta">CATEGORIES: <b>MAIN</b><br>BY <b>ADMIN</b></div>
  <div class="card-logo">BRIGHTWELL GIVING</div>
  <div class="card-date"><svg width="16" height="14" viewBox="0 0 16 14"><rect x="1" y="2" width="14" height="11" fill="none" stroke="#3e6b1f" stroke-width="1.5"/><path d="M1 5h14" stroke="#3e6b1f" stroke-width="1.5"/></svg>MAY 16, 2017</div>
  <div class="card-text">Brightwell Giving created the funds for helping the people in warm clothes to help others by giving donation.</div>
  <div class="card-btn">READ MORE</div>
</div>
<div class="abs card" style="left:482px;top:3337px">
  <div class="card-meta">CATEGORIES: <b>MAIN</b><br>BY <b>ADMIN</b></div>
  <div class="card-logo">BRIGHTWELL GIVING</div>
  <div class="card-date"><svg width="16" height="14" viewBox="0 0 16 14"><rect x="1" y="2" width="14" height="11" fill="none" stroke="#3e6b1f" stroke-width="1.5"/><path d="M1 5h14" stroke="#3e6b1f" stroke-width="1.5"/></svg>APRIL 28, 2017</div>
  <div class="card-text">We are starting the charity projects to collect funds on expanding.</div>
  <div class="card-btn">READ MORE</div>
</div>
<div class="abs card" style="left:759px;top:3337px">
  <div class="card-meta">CATEGORIES: <b>MAIN</b><br>BY <b>ADMIN</b></div>
  <div class="card-logo">BRIGHTWELL GIVING</div>
  <div class="card-date"><svg width="16" height="14" viewBox="0 0 16 14"><rect x="1" y="2" width="14" height="11" fill="none" stroke="#3e6b1f" stroke-width="1.5"/><path d="M1 5h14" stroke="#3e6b1f" stroke-width="1.5"/></svg>APRIL 12, 2017</div>
  <div class="card-text">Charity project love thy neighbor donation week.</div>
  <div class="card-btn">READ MORE</div>
</div>

<!-- contact -->
<div class="abs contact"></div>
<div class="abs section-title" style="top:3810px;font-size:32px;color:#fff">CONTACT US</div>
<div class="abs office" style="left:265px;top:3912px"><h3>NEW YORK OFFICE</h3><p>42 ORCHARD LN<br>ASHFORD NY 12001<br>(855)-555-0142</p></div>
<div class="abs office" style="left:485px;top:3912px"><h3>NY WAREHOUSE</h3><p>915 RIVER RD<br>MILLBROOK<br>NY 12402</p></div>
<div class="abs office" style="left:698px;top:3912px"><h3>THRIFT STORE</h3><p>268 MAPLE AVE<br>GLENPORT<br>NY 12510</p></div>

<div class="abs footer">© 2018 BRIGHTWELL GIVING. ALL RIGHTS RESERVED</div>

</body>
</html>
```